Coffee label for grocery store sales

We need a 3x4 label designed for our expanding grocery store market. I'm looking for something playful that will be eye catching on a shelf. Bag color is negotiable, but would prefer kraft, white, or black.

Target Market(s)

Grocery Stores

Industry/Entity Type

Coffee Shop

Logo Text

Heron Lane Coffee

Colors

Designer to choose colors to be used in the design.

Requirements
Must have
• Space for address label to identify blend.
• 47 W. Orchard Ave., Alder Falls, MN 55820
• www.heronlanecoffee.example
Nice to have
• Illustrations, bold colors

```html
<!DOCTYPE html>
<html lang="en">
<head>
<meta charset="utf-8">
<title>Heron Lane Coffee – Blend Label</title>
<link rel="stylesheet" href="https://fonts.googleapis.com/css2?family=Oswald:wght@500&family=Saira+Condensed:wght@600&display=swap">
<style>
  :root {
    --cream: #fde6cf;
    --roast: #2a231f;
    --bean-mid: #9c7f5a;
    --bean-dark: #4a3521;
  }
  * { box-sizing: border-box; margin: 0; padding: 0; }
  html, body { width: 900px; height: 1200px; overflow: hidden; }
  body { background: var(--cream); }

  .label {
    position: relative;
    width: 900px;
    height: 1200px;
    overflow: hidden;
    background: var(--cream);
  }

  .bean-pattern {
    position: absolute;
    inset: 0;
    background:
      radial-gradient(ellipse 62% 55% at 50% 50%, var(--bean-dark) 0%, var(--bean-mid) 55%, rgba(156,127,90,0.35) 80%, var(--cream) 100%);
  }

  .plate {
    position: absolute;
    inset: 0;
    width: 900px;
    height: 1200px;
  }

  .content {
    position: absolute;
    left: 150px;
    width: 600px;
    top: 0;
    height: 1200px;
    text-align: center;
    color: var(--roast);
  }

  .brand {
    position: absolute;
    top: 276px;
    left: 0;
    right: 0;
    font-family: "Saira Condensed", "Arial Narrow", sans-serif;
    font-weight: 600;
    font-size: 72px;
    line-height: 124px;
    letter-spacing: 2px;
    font-variant: small-caps;
    color: var(--roast);
  }

  .blend-title {
    position: absolute;
    top: 588px;
    left: 55px;
    right: 55px;
    height: 96px;
    border-top: 2px solid var(--roast);
    border-bottom: 2px solid var(--roast);
    font-family: "Oswald", sans-serif;
    font-weight: 500;
    font-size: 80px;
    line-height: 92px;
    letter-spacing: 1px;
  }

  .address {
    position: absolute;
    top: 747px;
    left: 0;
    right: 0;
    font-family: "Saira Condensed", "Arial Narrow", sans-serif;
    font-weight: 600;
    font-size: 46px;
    line-height: 56px;
    font-style: normal;
    letter-spacing: 1px;
  }

  .website {
    position: absolute;
    top: 876px;
    left: 0;
    right: 0;
    font-family: "Saira Condensed", "Arial Narrow", sans-serif;
    font-weight: 600;
    font-size: 36px;
    line-height: 48px;
    letter-spacing: 1px;
  }
</style>
</head>
<body>
<main class="label">
  <div class="bean-pattern" role="img" aria-label="Diagonal cream stripes over a roasted coffee bean pattern with distressed edges"></div>

  <svg class="plate" viewBox="0 0 900 1200" aria-hidden="true">
    <path fill="var(--cream)" stroke="var(--roast)" stroke-width="12"
      d="M150 265 A30 30 0 0 0 180 235 C300 235 360 160 450 160 C540 160 600 235 720 235 A30 30 0 0 0 750 265 L750 935 A30 30 0 0 0 720 965 C600 965 540 1028 450 1028 C360 1028 300 965 180 965 A30 30 0 0 0 150 935 Z"/>
    <path fill="none" stroke="var(--roast)" stroke-width="3"
      transform="translate(450 594) scale(0.965 0.975) translate(-450 -594)"
      d="M150 265 A30 30 0 0 0 180 235 C300 235 360 160 450 160 C540 160 600 235 720 235 A30 30 0 0 0 750 265 L750 935 A30 30 0 0 0 720 965 C600 965 540 1028 450 1028 C360 1028 300 965 180 965 A30 30 0 0 0 150 935 Z"/>
  </svg>

  <section class="content">
    <h1 class="brand">Heron Lane<br>Coffee</h1>
    <h2 class="blend-title">BLEND</h2>
    <address class="address">47 W. Orchard Ave.,<br>Alder Falls, MN 55820</address>
    <p class="website">www.heronlanecoffee.example</p>
  </section>
</main>
</body>
</html>
```